Business Card Design

Like white and Blue with gold border

Industry/Entity Type

Business

Contact Information for Business Card

CLEARVIEW LEDGER AND BOOKKEEPING SERVICE
Registered Tax Agent
PO Box 815 or 167 Marlowe Street Pellbrook Q. 4712
Phone 07 46135902
Fax 07 46138417
clearledger@varnellpartners.com
Senior Tax Preparer - MAVIS COLBRIDGE

Requirements
Must have
• on back of card should have - Appointment Date and time

```html
<!DOCTYPE html>
<html lang="en">
<head>
<meta charset="utf-8">
<title>Clearview Ledger and Bookkeeping Service – Business Card</title>
<link href="https://fonts.googleapis.com/css2?family=Nunito:wght@400;600;800&display=swap" rel="stylesheet">
<style>
  :root {
    --page: #ffffff;
    --card: #f4f4f4;
    --ink: #1e1e1e;
    --ink-soft: #2e2e2e;
    --mark: #8a8a8a;
    --tab: #050505;
    --shadow: rgba(0,0,0,0.35);
  }
  * { margin: 0; padding: 0; box-sizing: border-box; }
  html, body { width: 1200px; height: 1000px; overflow: hidden; background: var(--page); }
  body { position: relative; font-family: "Nunito", sans-serif; color: var(--ink); }

  .card {
    position: absolute; left: 271px; width: 685px; height: 422px;
    background: var(--card);
    box-shadow: 1px 2px 4px var(--shadow);
    overflow: hidden;
  }
  .card--front { top: 58px; }
  .card--back { top: 537px; }

  .brand { position: absolute; display: flex; align-items: flex-start; gap: 20px; }
  .card--front .brand { left: 141px; top: 46px; }
  .card--back .brand { left: 199px; top: 71px; }
  .brand__square { width: 76px; height: 76px; background: var(--mark); margin-top: 2px; }
  .brand__name {
    font-weight: 800; font-size: 24px; line-height: 32px; letter-spacing: 0.2px;
    text-transform: uppercase; color: var(--ink);
  }
  .brand__tagline {
    font-weight: 400; font-size: 20px; letter-spacing: 2.6px; line-height: 18px; color: var(--ink-soft);
  }

  .person { position: absolute; right: 29px; top: 156px; text-align: right; }
  .person__name { font-weight: 800; font-size: 26px; letter-spacing: 1.8px; line-height: 30px; }
  .person__role { font-weight: 400; font-size: 19px; letter-spacing: 0.6px; line-height: 26px; color: var(--ink-soft); }

  .contacts { position: absolute; left: 40px; top: 242px; list-style: none; }
  .contacts li { display: flex; align-items: flex-start; font-size: 16.5px; line-height: 16px; letter-spacing: 0.3px; }
  .contacts svg { width: 24px; flex: none; fill: var(--ink); margin-right: 22px; }
  .contacts .addr { height: 34px; }
  .contacts .addr svg { height: 30px; }
  .contacts .phone { margin-top: 8px; height: 24px; }
  .contacts .phone svg { height: 18px; }
  .contacts .mail { height: 28px; }
  .contacts .mail svg { height: 16px; }
  .contacts .fax svg { height: 24px; }
  .contacts .fax span { padding-top: 5px; }

  .tab {
    position: absolute; bottom: 0; width: 286px; height: 49px;
    background: var(--tab); border-radius: 24px 24px 0 0;
  }
  .card--front .tab { left: 197px; }
  .card--back .tab { left: 199px; }

  .appointment { position: absolute; left: 61px; top: 232px; }
  .appointment__title { font-weight: 800; font-size: 22px; letter-spacing: 0.8px; line-height: 28px; }
  .appointment__row { display: flex; align-items: flex-end; margin-top: 10px; font-size: 22px; letter-spacing: 1px; line-height: 28px; color: var(--ink-soft); }
  .appointment__label { width: 76px; }
  .appointment__line { width: 298px; border-bottom: 1.5px solid var(--ink); margin-bottom: 6px; }
</style>
</head>
<body>

<section class="card card--front">
  <div class="brand">
    <div class="brand__square"></div>
    <div>
      <div class="brand__name">Clearview Ledger &amp;<br>Bookkeeping Service</div>
      <div class="brand__tagline">Registered Tax Agent</div>
    </div>
  </div>

  <div class="person">
    <div class="person__name">MAVIS COLBRIDGE</div>
    <div class="person__role">Senior Tax Preparer</div>
  </div>

  <ul class="contacts">
    <li class="addr">
      <svg viewBox="0 0 24 30" aria-hidden="true"><path d="M12 0C6.5 0 3 4 3 9c0 6.5 9 21 9 21s9-14.5 9-21c0-5-3.5-9-9-9zm0 13a4 4 0 1 1 0-8 4 4 0 0 1 0 8z"/></svg>
      <span>PO Box 815 or 167,Marlowe Street<br>Pellbrook Q. 4712</span>
    </li>
    <li class="phone">
      <svg viewBox="0 0 24 24" aria-hidden="true"><path d="M6.6 10.8c1.4 2.8 3.8 5.1 6.6 6.6l2.2-2.2c.3-.3.7-.4 1-.2 1.1.4 2.300.6 3.6.6.6 0 1 .4 1 1V20c0 .6-.4 1-1 1C10.6 21 3 13.4 3 4c0-.6.4-1 1-1h3.5c.6 0 1 .4 1 1 0 1.3.2 2.5.6 3.6.1.3 0 .7-.2 1z"/></svg>
      <span>07 46135902</span>
    </li>
    <li class="mail">
      <svg viewBox="0 0 24 16" aria-hidden="true"><path d="M1 1h22v14H1z" fill="none" stroke="#1e1e1e" stroke-width="1.6"/><path d="M1 1l11 8 11-8" fill="none" stroke="#1e1e1e" stroke-width="1.6"/></svg>
      <span>clearledger@varnellpartners.com</span>
    </li>
    <li class="fax">
      <svg viewBox="0 0 24 24" aria-hidden="true"><rect x="0" y="6" width="6" height="18" rx="1"/><rect x="7" y="0" width="11" height="7"/><rect x="7" y="6" width="17" height="18" rx="1"/><g fill="#f4f4f4"><rect x="10" y="9" width="11" height="3"/><rect x="10" y="14" width="2.5" height="2.5"/><rect x="14" y="14" width="2.5" height="2.5"/><rect x="18" y="14" width="2.5" height="2.5"/><rect x="10" y="18" width="2.5" height="2.5"/><rect x="14" y="18" width="2.5" height="2.5"/><rect x="18" y="18" width="2.5" height="2.5"/></g></svg>
      <span>07 46138417</span>
    </li>
  </ul>

  <div class="tab"></div>
</section>

<section class="card card--back">
  <div class="brand">
    <div class="brand__square"></div>
    <div>
      <div class="brand__name">Clearview Ledger &amp;<br>Bookkeeping Service</div>
      <div class="brand__tagline">Registered Tax Agent</div>
    </div>
  </div>

  <div class="appointment">
    <div class="appointment__title">Appointment</div>
    <div class="appointment__row"><span class="appointment__label">Date</span><span class="appointment__line"></span></div>
    <div class="appointment__row"><span class="appointment__label">time</span><span class="appointment__line"></span></div>
  </div>

  <div class="tab"></div>
</section>

</body>
</html>
```